Boutique Soy Candle Company Needs a Label Design

We need a label design for a boutique soy candle company based in Robe, South Australia.
We sell high quality, hand poured soy wax candles, melts and reed diffusers.
We are based in a coastal town and would like the label to reflect our rustic, beachy, retro but luxurious feel. I've attached the design we've been using and like the idea but want to have something more professional. The picture of the Venner Spire is something that we would like to be included somehow - it's like our town symbol - a 'lighthouse' of sorts. It was quite stylised on my original design but we are open to different interpretations.
We like the idea of a 'Kraft' brown paper sort of label but are not set on it. We also love the fluro pink look.

```html
<!DOCTYPE html>
<html lang="en">
<head>
<meta charset="utf-8">
<title>Halcyon Soy Candle Co. – Label No. 004</title>
<link href="https://fonts.googleapis.com/css2?family=Open+Sans:wght@400;600;700&display=swap" rel="stylesheet">
<style>
  :root {
    --page: #ffffff;
    --label-cream: #f5f6ec;
    --band-white: #ffffff;
    --fluro-pink: #e8177a;
    --ink: #1a1a1a;
  }
  * { margin: 0; padding: 0; box-sizing: border-box; }
  html, body {
    width: 1200px;
    height: 1108px;
    overflow: hidden;
    background: var(--page);
    font-family: "Open Sans", Arial, sans-serif;
  }
  .label {
    position: absolute;
    left: 150px;
    top: 104px;
    width: 900px;
    height: 900px;
  }
  .label-shapes {
    position: absolute;
    inset: 0;
    width: 900px;
    height: 900px;
  }
  .label-text { position: absolute; white-space: nowrap; }

  .brand {
    left: 150px;
    top: 232px;
    width: 560px;
    color: var(--fluro-pink);
    font-weight: 700;
    line-height: 1;
  }
  .brand-name { display: block; font-size: 100px; letter-spacing: 1px; }
  .brand-sub { display: block; font-size: 32px; text-align: right; margin-top: 2px; }

  .origin {
    left: 104px;
    top: 443px;
    height: 125px;
    line-height: 125px;
    font-size: 34px;
    font-weight: 600;
    color: var(--ink);
  }
  .spec {
    top: 582px;
    text-align: center;
    font-size: 38px;
    font-weight: 600;
    line-height: 50px;
    color: var(--fluro-pink);
  }
  .spec-wax { left: 293px; width: 300px; }
  .spec-weight { left: 653px; width: 180px; }

  .scent {
    right: 445px;
    top: 722px;
    text-align: right;
    font-size: 28px;
    font-weight: 600;
    line-height: 44px;
    color: var(--ink);
  }
  .batch-divider {
    position: absolute;
    left: 467px;
    top: 724px;
    width: 3px;
    height: 86px;
    background: var(--ink);
  }
  .batch {
    left: 482px;
    top: 728px;
    color: var(--ink);
    line-height: 1;
  }
  .batch-label { display: block; font-size: 20px; font-weight: 600; }
  .batch-number { display: block; font-size: 58px; font-weight: 700; margin-top: 0; }
</style>
</head>
<body>
  <div class="label">
    <svg class="label-shapes" viewBox="0 0 900 900" aria-hidden="true">
      <defs>
        <clipPath id="label-edge"><circle cx="450" cy="450" r="450"/></clipPath>
      </defs>
      <g clip-path="url(#label-edge)">
        <rect width="900" height="900" fill="var(--label-cream)"/>
        <polygon class="pink-spire" points="745,155 900,225 900,830 605,830" fill="var(--fluro-pink)"/>
        <rect class="band-cream" x="0" y="568" width="900" height="125" fill="var(--label-cream)"/>
        <polygon class="band-white" points="0,443 684,443 657,568 0,568" fill="var(--band-white)"/>
        <polygon class="band-white" points="0,693 631,693 605,830 0,830" fill="var(--band-white)"/>
      </g>
    </svg>

    <div class="label-text brand">
      <span class="brand-name">Halcyon</span>
      <span class="brand-sub">soy candle co.</span>
    </div>

    <div class="label-text origin">HAND MADE IN WREN BAY, SA</div>

    <div class="label-text spec spec-wax">ALL NATURAL<br>SOY</div>
    <div class="label-text spec spec-weight">300<br>GRAMS</div>

    <div class="label-text scent">HONEY SUCKLE<br>JASMINE</div>
    <div class="batch-divider"></div>
    <div class="label-text batch">
      <span class="batch-label">NO.</span>
      <span class="batch-number">004</span>
    </div>
  </div>
</body>
</html>
```